New Zealand Luggage Importer Needs Business Cards

We need professional, creative and fashionable business cards created.
We are based in New Zealand and import and distribute high-end, quality, fashionable and durable luggage.
We pride ourselves on selling the very best quality luggage, second only to 1 brand (which we won't mention here)...we use the same manufacturer. However, our prices are much more reasonable.
Industry/Entity Type
Business
Contact Information for Business Card
Mark Dunsley
027 512 4068
3/17 Harlow Street, Pinecrest Flats, Auckland, 0614
PO Box 204377, Fernside, Auckland 0731
09-528-3916
sales@brivancases.co.nz / www.brivancases.co.nz

```html
<!DOCTYPE html>
<html lang="en">
<head>
<meta charset="utf-8">
<title>Brivan Cases – Business Cards</title>
<link href="https://fonts.googleapis.com/css2?family=Michroma&family=Open+Sans:wght@400&display=swap" rel="stylesheet">
<style>
  :root {
    --backdrop: #e9e6e3;
    --card: #272627;
    --gold: #c9a24e;
    --ink-light: #c4c4c4;
    --ink-muted: #a3a3a3;
    --white: #ffffff;
    --divider: #6b6b6b;
  }
  * { margin: 0; padding: 0; box-sizing: border-box; }
  html, body { width: 1200px; height: 900px; overflow: hidden; }
  body { background: var(--backdrop); position: relative; font-family: "Open Sans", sans-serif; }

  .card {
    position: absolute;
    background: var(--card);
    box-shadow: 0 6px 18px rgba(0,0,0,0.25);
  }
  .card--front { left: 78px; top: 34px; width: 588px; height: 364px; }
  .card--back { left: 388px; top: 505px; width: 567px; height: 352px; }

  .wordmark {
    position: absolute;
    left: 0; right: 0;
    text-align: center;
    font-family: "Michroma", sans-serif;
    color: var(--gold);
    letter-spacing: 1px;
    white-space: nowrap;
  }
  .card--front .wordmark { top: 60px; font-size: 31px; }
  .card--back .wordmark { top: 156px; font-size: 30px; }

  .holder-name {
    position: absolute;
    top: 158px; left: 0; right: 0;
    text-align: center;
    font-family: "Michroma", sans-serif;
    font-size: 21px;
    color: var(--gold);
    letter-spacing: 1px;
  }

  .contact {
    position: absolute;
    top: 214px;
    font-size: 15px;
    color: var(--ink-light);
    line-height: 23px;
  }
  .contact--left { right: 302px; text-align: right; }
  .contact--right { left: 305px; }
  .contact-row { display: flex; align-items: center; gap: 6px; white-space: nowrap; }
  .contact--left .contact-row { justify-content: flex-end; }
  .contact-row svg { width: 12px; height: 12px; fill: var(--gold); flex: none; }

  .contact-divider {
    position: absolute;
    left: 294px; top: 214px;
    width: 1px; height: 44px;
    background: var(--divider);
  }

  .address {
    position: absolute;
    top: 276px; left: 0; right: 0;
    text-align: center;
    font-size: 15.5px;
    line-height: 27px;
    color: var(--ink-muted);
  }

  .site-url {
    position: absolute;
    top: 288px; left: 0; right: 0;
    text-align: center;
    font-size: 16px;
    color: var(--white);
    letter-spacing: 0.5px;
  }
  .site-url .site-name { color: var(--gold); }
</style>
</head>
<body>

<section class="card card--front" aria-label="Business card front">
  <div class="wordmark">BRIVAN CASES</div>
  <div class="holder-name">MARK DUNSLEY</div>

  <div class="contact contact--left">
    <div class="contact-row">027 512 4068
      <svg viewBox="0 0 24 24" aria-hidden="true"><path d="M6.6 10.8a15.1 15.1 0 0 0 6.6 6.6l2.2-2.2a1 1 0 0 1 1-.25 11.4 11.4 0 0 0 3.6.57 1 1 0 0 1 1 1V20a1 1 0 0 1-1 1A17 17 0 0 1 3 4a1 1 0 0 1 1-1h3.5a1 1 0 0 1 1 1c0 1.25.2 2.45.57 3.57a1 1 0 0 1-.25 1z"/></svg>
    </div>
    <div class="contact-row">www.brivancases.co.nz
      <svg viewBox="0 0 24 24" aria-hidden="true"><circle cx="12" cy="12" r="10"/><path d="M2 12h20M12 2a15 15 0 0 1 0 20M12 2a15 15 0 0 0 0 20" stroke="#272627" stroke-width="1.6" fill="none"/></svg>
    </div>
  </div>

  <div class="contact-divider"></div>

  <div class="contact contact--right">
    <div class="contact-row">
      <svg viewBox="0 0 24 24" aria-hidden="true"><path d="M7 1h10a2 2 0 0 1 2 2v18a2 2 0 0 1-2 2H7a2 2 0 0 1-2-2V3a2 2 0 0 1 2-2zm0 3v14h10V4z"/></svg>09-528-3916
    </div>
    <div class="contact-row">
      <svg viewBox="0 0 24 24" aria-hidden="true"><path d="M2 5h20v14H2z"/><path d="M2 5l10 8 10-8" stroke="#272627" stroke-width="1.8" fill="none"/></svg>sales@brivancases.co.nz
    </div>
  </div>

  <div class="address">
    <p>3/17 Harlow Street, Pinecrest Flats, Auckland, 0614</p>
    <p>PO Box 204377, Fernside, Auckland 0731</p>
  </div>
</section>

<section class="card card--back" aria-label="Business card back">
  <div class="wordmark">BRIVAN CASES</div>
  <div class="site-url">www.<span class="site-name">brivancases</span>.co.nz</div>
</section>

</body>
</html>
```